Looking to design a new sign for our church.

Looking for a new sign
4 x 8 feet dimension
We are renaming the church "Medlow Ridge Community Church"
looking for legible graphics
Would like some type of backdrop being a family tree (oak) / open to other ideas as you are led
I have included a pic of the old sign for your review
would like to incorporate our Open Door Missions on the lower right hand corner of the sign / see file attached

```html
<!DOCTYPE html>
<html lang="en">
<head>
<meta charset="utf-8">
<title>Medlow Ridge Community Church – Sign</title>
<link rel="stylesheet" href="https://fonts.googleapis.com/css2?family=Montserrat:wght@900&family=Oswald:wght@500;600&family=Yellowtail&display=block">
<style>
  :root {
    --ink: #0a0a0a;
    --paper: #ffffff;
    --backdrop: #e9e9e7;
    --tree-tone: #161616;
  }
  html, body {
    margin: 0;
    padding: 0;
    width: 1093px;
    height: 1200px;
    overflow: hidden;
    background: var(--backdrop);
  }
  .sign {
    position: absolute;
    left: 0;
    top: 327px;
    width: 1093px;
    height: 545px;
    display: block;
    background: var(--paper);
  }
  .church-name {
    font-family: "Montserrat", Arial, sans-serif;
    font-weight: 900;
    fill: var(--ink);
  }
  .church-sub {
    font-family: "Oswald", "Arial Narrow", sans-serif;
    font-weight: 600;
    fill: var(--ink);
  }
  .church-script {
    font-family: "Yellowtail", "Brush Script MT", cursive;
    fill: var(--ink);
  }
  .service-time,
  .service-name,
  .ministry-name {
    font-family: "Oswald", "Arial Narrow", sans-serif;
    font-weight: 600;
    fill: var(--ink);
  }
  .band { fill: var(--ink); }
  .notch { fill: var(--paper); }
  .tree-area { fill: var(--tree-tone); }
  .ministry-mark { fill: none; stroke: var(--ink); stroke-width: 3; }
</style>
</head>
<body>
<svg class="sign" viewBox="0 0 1093 545" xmlns="http://www.w3.org/2000/svg">
  <!-- top accent bar -->
  <rect class="band" x="210" y="0" width="673" height="31"/>

  <!-- church name -->
  <text class="church-name" x="57" y="134" font-size="104" textLength="979" lengthAdjust="spacingAndGlyphs">MEDLOW RIDGE</text>
  <text class="church-sub" x="116" y="229" font-size="84" textLength="375" lengthAdjust="spacingAndGlyphs">COMMUNITY</text>
  <text class="church-script" x="199" y="339" font-size="118" textLength="289" lengthAdjust="spacingAndGlyphs">Church</text>

  <!-- oak tree backdrop -->
  <rect class="tree-area" x="0" y="240" width="108" height="222" rx="40" role="img" aria-label="Silhouette of a broad oak tree standing on a low hill"/>

  <!-- ground band with notch -->
  <rect class="band" x="0" y="458" width="1093" height="87"/>
  <circle class="notch" cx="544" cy="434" r="92"/>

  <!-- ministry mark -->
  <text class="ministry-name" font-size="20" text-anchor="middle">
    <tspan x="544" y="336">OPEN DOOR</tspan>
    <tspan x="544" y="360">MISSIONS</tspan>
  </text>
  <circle class="ministry-mark" cx="544" cy="430" r="52"/>

  <!-- service times -->
  <text class="service-time" x="642" y="185" font-size="28">10:30 am</text>
  <text class="service-name" x="642" y="235" font-size="52" textLength="309" lengthAdjust="spacingAndGlyphs">Worship Service</text>

  <text class="service-time" x="646" y="286" font-size="28">9:30 am</text>
  <text class="service-name" x="645" y="333" font-size="52" textLength="282" lengthAdjust="spacingAndGlyphs">Sunday School</text>

  <text class="service-time" x="646" y="382" font-size="28">6:00 am</text>
  <text class="service-name" x="645" y="434" font-size="52" textLength="352" lengthAdjust="spacingAndGlyphs">Wednesday Service</text>
</svg>
</body>
</html>
```